Roofing Contractor business card redesign

I want to redesign my business card with a fresh, eye catching concept

Target Market(s)

Residential Roofing Clients, potential employees, and subcontractors.

Industry/Entity Type

Business

Colors

Designer to choose colors to be used in the design.

Requirements
Nice to have
• I just want something that's more pleasing to the eye. You can use a combination of either / or of my logos.

```html
<!DOCTYPE html>
<html lang="en">
<head>
<meta charset="utf-8">
<title>Fair Hand Builders – Business Card</title>
<link href="https://fonts.googleapis.com/css2?family=Roboto+Condensed:wght@400;700;900&display=swap" rel="stylesheet">
<style>
  :root {
    --bg: #2b2b2b;
    --brown: #4a2a24;
    --brown-dark: #3a1f1a;
    --orange: #f08a1c;
    --yellow: #f6c21a;
    --white: #ffffff;
    --ink: #3b2520;
    --muted: #8a7a74;
  }
  * { margin: 0; padding: 0; box-sizing: border-box; }
  html, body { width: 1200px; height: 660px; overflow: hidden; }
  body {
    background: var(--bg);
    font-family: "Roboto Condensed", Arial, sans-serif;
    position: relative;
  }
  .card {
    position: absolute;
    top: 175px;
    width: 540px;
    height: 310px;
    background: var(--white);
    overflow: hidden;
    box-shadow: 0 10px 30px rgba(0,0,0,.45);
  }
  .card--front { left: 40px; }
  .card--back { left: 620px; }

  /* front */
  .band { position: absolute; left: 0; width: 100%; background: var(--brown); }
  .band--top { top: 0; height: 82px; }
  .band--bottom { bottom: 0; height: 78px; }
  .stripe { position: absolute; left: 0; width: 100%; height: 7px;
    background: linear-gradient(var(--yellow) 0 55%, var(--orange) 55% 100%); }
  .stripe--top { top: 82px; }
  .stripe--bottom { bottom: 78px; transform: scaleY(-1); }
  .front-brand {
    position: absolute; top: 89px; bottom: 85px; left: 0; right: 0;
    display: flex; align-items: center; justify-content: center; gap: 14px;
  }
  .brand-dot { width: 44px; height: 44px; border-radius: 50%; background: var(--orange); flex: none; }
  .brand-name {
    font-weight: 900; color: var(--ink); font-size: 40px; line-height: 1;
    letter-spacing: -0.5px;
  }

  /* back */
  .back-logo {
    position: absolute; left: 30px; top: 70px; width: 200px; height: 160px;
    display: flex; flex-direction: column; align-items: center; justify-content: center; gap: 12px;
  }
  .back-logo .brand-dot { width: 70px; height: 70px; }
  .back-logo .brand-name { font-size: 26px; text-align: center; }
  .divider { position: absolute; left: 255px; top: 55px; width: 1px; height: 175px; background: var(--muted); }
  .contact { position: absolute; left: 285px; top: 62px; color: var(--ink); }
  .contact__name { font-size: 24px; font-weight: 700; line-height: 1.1; }
  .contact__role { font-size: 14px; color: var(--orange); line-height: 1.25; }
  .contact__list { list-style: none; margin-top: 14px; font-size: 14px; line-height: 1.35; }
  .contact__list li { display: flex; gap: 8px; align-items: flex-start; }
  .contact__list svg { width: 13px; height: 13px; flex: none; margin-top: 3px; fill: var(--orange); }
  .contact__list .no-icon { padding-left: 21px; }
  .back-stripe { position: absolute; left: 0; bottom: 46px; width: 100%; height: 7px;
    background: linear-gradient(var(--orange) 0 45%, var(--yellow) 45% 100%); }
  .back-band { position: absolute; left: 0; bottom: 0; width: 100%; height: 46px; background: var(--brown); }
</style>
</head>
<body>
  <section class="card card--front" aria-label="Card front">
    <div class="band band--top"></div>
    <div class="stripe stripe--top"></div>
    <div class="front-brand">
      <span class="brand-dot"></span>
      <span class="brand-name">Fair Hand Builders, Inc.</span>
    </div>
    <div class="stripe stripe--bottom"></div>
    <div class="band band--bottom"></div>
  </section>

  <section class="card card--back" aria-label="Card back">
    <div class="back-logo">
      <span class="brand-dot"></span>
      <span class="brand-name">Fair Hand Builders, Inc.</span>
    </div>
    <div class="divider"></div>
    <div class="contact">
      <p class="contact__name">Dale Mercer</p>
      <p class="contact__role">Keller Certified Roof Inspector</p>
      <p class="contact__role">Licensed Property Adjuster</p>
      <ul class="contact__list">
        <li><svg viewBox="0 0 16 16"><path d="M3 1l3 3-2 2c1 2 3 4 5 5l2-2 3 3-2 3C6 15 1 10 1 3z"/></svg>(555) 218-4000</li>
        <li><svg viewBox="0 0 16 16"><path d="M4 0h8a1 1 0 011 1v14a1 1 0 01-1 1H4a1 1 0 01-1-1V1a1 1 0 011-1zm1 2v10h6V2z"/></svg>(555) 730-6142</li>
        <li><svg viewBox="0 0 16 16"><path d="M0 3h16v10H0zm1 1v1l7 4 7-4V4z"/></svg>dale@fairhandtx.com</li>
        <li><svg viewBox="0 0 16 16"><path d="M8 0a5 5 0 015 5c0 4-5 11-5 11S3 9 3 5a5 5 0 015-5zm0 3a2 2 0 100 4 2 2 0 000-4z"/></svg>4410 Cedar Lane Suite 118</li>
        <li class="no-icon">Plano, TX 75093</li>
      </ul>
    </div>
    <div class="back-stripe"></div>
    <div class="back-band"></div>
  </section>
</body>
</html>
```